◆遺体の目的/概要
電子書籍(novrel)の表紙のデザインをお願いします。

◆画像のサイズ
表紙ファイルの理想的な寸法は2,560✕1,600ピクセルです。
注:画像の寸法は1,000✕625ピクセル以上であることが必要です。
画像の最大の寸法は10,000✕10,000ピクセルです。

◆タイトル
外国人と一緒に働くすべての人へ
「ソラーレ・ポルト・メトリクス」
Solare Porto Metrics
少子高齢化の社会を生き残る強い会社を作る方法

◆著者
外国人ブリッジコーディネーター
橋本 健吾

◆本の内容
少子高齢化が進む社会にあって、
外国人労働者の必要性や、彼らが働きやす職場環境作りの必要性
どんなコミュニケーションが必要かという事を解説した本です。
※本文を参考資料として添付します。

◆デザイン要望
会社や企業向けなので、プロフェッショナルなイメージ
グローバルなイメージ(目を引く外国人の写真など)
でよろしくお願い致します。

※次点、次々点の方への参加報酬も設定いたします。

※その他、必要な情報がありましたらお問い合せください。

本文の内容に該当する登場人物のイメージを用いている点や
「強い会社を作る」という主なテーマが強調されていいる点など、
ぱっと見て分かりやすいものを選ばせていただきました。

ほんとにどれもセンスを感じられるものだったので、
選定するのに、とても時間がかかりました。
同じテーマで、こんなにも色々なアイデアがあること
その多様性に感動しました。
皆さんが時間をかけて、考えてくださったことに感謝致します。
今後も出版を考えていますので、また依頼の際は多くの方の提案をよろしくお願い致します!

```html
<!DOCTYPE html>
<html lang="ja">
<head>
<meta charset="utf-8">
<title>ソラーレ・ポルト・メトリクス</title>
<link rel="stylesheet" href="https://fonts.googleapis.com/css2?family=Noto+Sans+JP:wght@500;700;900&family=Roboto:wght@700;900&display=swap">
<style>
  :root {
    --ink: #111111;
    --white: #ffffff;
    --accent: #e2452e;
    --sky-top: #cfeef4;
    --sky-bottom: #ffffff;
    --photo-dark: #2a2f38;
    --photo-mid: #5d6674;
    --photo-light: #b9c1cb;
  }
  * { margin: 0; padding: 0; box-sizing: border-box; }
  html, body { width: 750px; height: 1200px; overflow: hidden; }
  body { background: var(--white); font-family: "Noto Sans JP", sans-serif; }
  .cover {
    position: relative;
    width: 750px; height: 1200px;
    background: linear-gradient(180deg, var(--sky-top) 0%, var(--sky-bottom) 55%);
    overflow: hidden;
  }
  .cover-photo {
    position: absolute; left: 0; top: 0;
    width: 750px; height: 555px;
    background:
      radial-gradient(ellipse 55% 45% at 50% 50%, #c9a58d 0%, rgba(201,165,141,0) 70%),
      linear-gradient(180deg, var(--photo-dark) 0%, var(--photo-mid) 45%, var(--photo-light) 100%);
  }
  .tagline {
    position: absolute; left: 0; top: 0; width: 100%;
    padding-top: 22px;
    text-align: center; color: var(--white);
    font-weight: 700; font-size: 33px; line-height: 50px;
    letter-spacing: 1px;
  }
  .title {
    position: absolute; left: 0; width: 100%;
    text-align: center; color: var(--ink);
    font-family: "Roboto", sans-serif; font-weight: 900;
    line-height: 1;
  }
  .title-line1 { top: 585px; font-size: 150px; }
  .title-line2 { top: 700px; font-size: 150px; }
  .title-line3 { top: 828px; font-size: 84px; }
  .subtitle {
    position: absolute; left: 0; top: 930px; width: 100%;
    text-align: center; color: var(--accent);
    font-weight: 900; font-size: 30px;
  }
  .author-role {
    position: absolute; left: 0; top: 1070px; width: 100%;
    text-align: center; color: var(--ink);
    font-weight: 500; font-size: 29px;
  }
  .author-name {
    position: absolute; left: 0; top: 1118px; width: 100%;
    text-align: center; color: var(--ink);
    font-weight: 500; font-size: 44px; letter-spacing: 4px;
  }
</style>
</head>
<body>
  <main class="cover">
    <div class="cover-photo" role="img" aria-label="ビジネススーツ姿の多国籍の人々が円陣を組み、手を重ね合わせている写真"></div>
    <p class="tagline">外国人と一緒に働くすべての人へ<br>「ソラーレ・ポルト・メトリクス」</p>
    <h1>
      <span class="title title-line1">Solare</span>
      <span class="title title-line2">Porto</span>
      <span class="title title-line3">Metrics</span>
    </h1>
    <p class="subtitle">少子高齢化の社会を生き残る強い会社を作る方法</p>
    <p class="author-role">外国人ブリッジコーディネーター</p>
    <p class="author-name">橋本 健吾</p>
  </main>
</body>
</html>
```